Designer Furniture: Brochure Design | Price List | Price Cards

1. brochure 2. price list 3. showroom price cards

We need a brochure design of our high-end wood and acrylic furniture line. We are a custom plastics & acrylics manufacturing company - one facet of our business is custom high-end furniture. We have developed our own proprietary designer furniture line and need a brochure and supporting price list and showroom price cards to reflect the furniture's unique wood and acrylic high-end design appeal.

****More supporting informational & graphic files at:****
https://www.filenook.example/sh/qpwerm7vtbkx3aa/RtyuPlMnBv

We would like to see the following design style: European, modern, clean lines | Lots of white | warm greys | minimalistic in "graphic design" to show off our "furniture design" as the primary focus of the brochure "less is more" | we work in the high-end design market so our look and feel has to reflect that of 'design' | a screenshot of an example of what we like is included in supplied files | we like modern artwork

This is a North American print distribution. Further detailed instructions & details are supplied in the supporting uploaded files of the project.

The winning design may lead to future exclusive design work in this particular facet of our business - possibly others.

* Price list: should be editable PDF (printed on in-house monochrome laser) that is a secondary insert in to the brochure - B&W 6.75"x8.25" Portrait. Includes each item in table or catalogue-type format with dimensions and pricing "$###.##"

* Showroom price card: editable PDF file for each piece of furniture. 5"x7" Portrait OR Landscape. Should include the main 2D dimensional line drawing of each piece along with dimensions and Brookvale Logo or Icon and QRCode from OLD brochure design.
Updates

*****Supporting files & graphic files at:******

- It is imperative that all 3D renderings from our "Rendering" folder in dropbox link be shown in our brochure.

- The price list is a monochrome listing of all our pieces of furniture with dimensions and prices in a table or catalogue-type format.

Here's to clear up some of the questions you've been asking:

PRICE CARDS:
5"x7" portrait
These cards will be but in to an acrylic stand and sit on each piece of furniture - so would probably be best to design a front and back.
Side #1 with specifics: Product name, product number, dimensions, line drawing, price, Brookvale Logo, QR Code, Contact info
Side #2 the other showcasing 3D image, Product Name, Brookvale logo

PRICE SHEET INSERT:
This is an insert for the brochure cataloguing each of the products, 2D dimensional line drawing, dimensions, product name, product number, price - editable PDF so we can easily change prices and print on our in-house monochrome (black & white) printer. 1 or 2 sided - doesn't matter.  Will fit inside the brochure, so cannot be any larger than 7x8.5 - I would suggest to make .25" smaller than brochure folded size - 6.75x8.25

Target Market(s)

Designers, Architects and High-end Retail Furniture Outlets

Industry/Entity Type

Business

Requirements
Must have
• - Brochure finished folded size must be: 7”w x 8.5”h (PORTRAIT)
- raw print stock is 12.5”x19” – maximum print area is 12”x18.5”
- as long as finished folded size is exactly 7”x8.5” portrait - folding style is up to designer (bifold, 3-panel roll, 4-panel roll)
- Will be digitally printed - RGB on 80lb gloss text
- 3D Render image of each product in the furniture line must be included...see below

****More supporting files & graphic files at:****
Nice to have
• ****Supporting files & graphic files at:****

```html
<!DOCTYPE html>
<html lang="en">
<head>
<meta charset="utf-8">
<title>Brookvale Collection – Brochure Inside Spread</title>
<link rel="stylesheet" href="https://fonts.googleapis.com/css2?family=Archivo+Narrow:wght@400&family=PT+Sans:wght@400&display=swap">
<style>
  :root {
    --canvas-bg: #ffffff;
    --page-bg: #ffffff;
    --page-edge: #e2e2e2;
    --gutter-shade: rgba(0,0,0,0.06);
    --body-text: #8a8a8a;
    --title-ink: rgba(40,34,28,0.72);
    --interior-warm: #c9bba6;
    --interior-mid: #6e5f4e;
    --city-night: #3c3a74;
    --city-glow: #5b4f8c;
  }
  * { box-sizing: border-box; margin: 0; padding: 0; }
  html, body {
    width: 1200px; height: 1000px; overflow: hidden;
    background: var(--canvas-bg);
  }
  .spread {
    position: absolute; left: 53px; top: 205px;
    width: 1102px; height: 672px;
    background: var(--page-bg);
    border: 1px solid var(--page-edge);
  }
  .spread__fold {
    position: absolute; left: 551px; top: 0; width: 40px; height: 100%;
    background: linear-gradient(to right, var(--gutter-shade), rgba(0,0,0,0));
  }
  .hero-image {
    position: absolute; left: 40px; top: 42px;
    width: 1018px; height: 408px;
    background:
      linear-gradient(to bottom, rgba(0,0,0,0) 60%, rgba(60,50,40,0.35) 100%),
      linear-gradient(to right, var(--interior-warm) 0%, #a8977f 25%, var(--interior-mid) 48%, var(--city-glow) 62%, var(--city-night) 100%);
  }
  .hero-title {
    position: absolute; right: 48px; top: 372px;
    font-family: "PT Sans", sans-serif;
    font-size: 66px; line-height: 1; letter-spacing: -0.5px;
    color: var(--title-ink);
  }
  .copy {
    position: absolute; top: 463px;
    font-family: "Archivo Narrow", sans-serif;
    font-size: 10.4px; line-height: 14.4px;
    color: var(--body-text);
  }
  .copy p + p { margin-top: 14px; }
  .copy--col-a { left: 40px; width: 228px; }
  .copy--col-b { left: 282px; width: 232px; }
  .copy--col-c { left: 588px; width: 474px; }
</style>
</head>
<body>
  <main class="spread">
    <div class="hero-image" role="img" aria-label="Interior rendering of Brookvale wood and clear acrylic furniture: lamp, side table, armchair, desk and bench in front of windows overlooking a city at night"></div>
    <h1 class="hero-title">Organic Modern</h1>
    <div class="spread__fold"></div>

    <section class="copy copy--col-a">
      <p>The Brookvale Collection celebrates the complexities of nature by juxtaposing the non-linear “blue-stain” ribbon that permeates each unique piece of wood with the clean lines and transparency of the synthetic-based Clarite.</p>
      <p>Each piece of this line carries clean, rectangular lines and edges. Each remains faithful to the urban design appeal yet showcases the natural warmth and softness of the wood hovering in the face of gravity.</p>
    </section>

    <section class="copy copy--col-b">
      <p>The Brookvale collection is a tribute to the 800 million cubic metres of Lodgepole Pine that have been killed by the Mountain Pine Beetle (MPB) in the Interior of British Columbia.</p>
      <p>The pieces are named using words from Chinook Jargon. Chinook Jargon was the unifying trade language of the Pacific Northwest during the 19th century. It was the working language in many of the towns and communities in British Columbia that have been most impacted by the devastation of the Mountain Pine Beetle.</p>
    </section>

    <section class="copy copy--col-c">
      <p>The Mountain Pine Beetle naturally “blue-stained” pine beams we incorporate into our Brookvale furniture is considered a natural artisan product - each one completely and truly unique. Checking, knots, and minor cupping are considered part of each piece’s natural, individualistic and inconsistent aesthetic appeal.</p>
      <p>Larkspur is the foremost manufacturer of high-end, custom, build-to-order acrylic and clarite furniture for both residential and commercial customers since 1978. In keeping with Larkspur’s enduring philosophy, each piece of our signature furniture line is crafted from the highest quality materials - selected, fabricated and hand-crafted right in British Columbia, Canada.</p>
      <p>Please contact us to order or to request a custom design for your specifications.</p>
    </section>
  </main>
</body>
</html>
```